Container Web Design Project

I need the front page of my website to have a new, fresh look.
Our company is a highly specialized marketplace for shipping containers (yes, the 20' and 40' kind). Basically, think of Quibzo for shipping containers.
I have all of the links/content that I need plugged into a wireframe (attached), and the core color (blue #0073a2) of our existing site should stay the same as we've got stationary, business cards, marketing materials...
If you have any questions please ask.

```html
<!DOCTYPE html>
<html lang="en">
<head>
<meta charset="utf-8">
<title>CrateHarbor.com – Shipping Container Marketplace</title>
<link href="https://fonts.googleapis.com/css2?family=Gelasio:wght@400;700&family=Open+Sans:wght@400;600;700&display=swap" rel="stylesheet">
<style>
:root{
  --brand:#0073a2;
  --brand-dark:#00506f;
  --brand-deep:#003a52;
  --nav-btn:#9ad9f2;
  --nav-btn-edge:#5fb7dc;
  --side-bg:#b4edf6;
  --panel:#ffffff;
  --ink:#111111;
  --muted:#333333;
  --footer:#003c55;
  --carousel-bg:#e6e6e6;
}
*{box-sizing:border-box;margin:0;padding:0}
html,body{width:995px;height:1200px;overflow:hidden}
body{position:relative;background:var(--side-bg);font-family:"Gelasio",serif;color:var(--ink)}
.abs{position:absolute}

.site-header{left:0;top:0;width:995px;height:107px;background:linear-gradient(180deg,#0a7fb0 0%,var(--brand) 45%,var(--brand-dark) 100%)}
.brand-name{left:20px;top:4px;width:149px;height:34px;border:2px solid #fff;color:#fff;font:700 19px/30px "Gelasio",serif;text-align:center}
.top-links{right:30px;top:4px;display:flex;gap:22px;color:#fff;font-size:15px}
.main-nav a{position:absolute;top:49px;height:20px;background:var(--nav-btn);border:1px solid var(--nav-btn-edge);color:#0b2a3a;font-size:13px;line-height:18px;text-align:center}
.search-input{left:356px;top:80px;width:275px;height:18px;background:#cfd6da;border:1px solid #8a979e;border-radius:3px;font-size:13px;line-height:16px;padding-left:8px;color:#555}
.select{top:80px;height:18px;background:#e5e8ea;border:1px solid #8a979e;font:11px/16px "Open Sans",sans-serif;padding-left:5px;color:#222}
.select svg{position:absolute;right:2px;top:2px}
.search-btn{left:827px;top:81px;width:57px;height:16px;background:#e5e8ea;border:1px solid #8a979e;border-radius:2px;font-size:10px;line-height:14px;text-align:center}

.content-panel{left:337px;top:107px;width:644px;height:1003px;background:var(--panel)}

.side-nav a{position:absolute;left:24px;width:297px;height:24px;background:linear-gradient(180deg,#1b8fbf,var(--brand) 50%,var(--brand-dark));border:1px solid var(--brand-deep);color:#fff;font-size:15px;line-height:22px;text-align:center}
.newsletter-label{left:23px;top:420px;font-size:13px;font-weight:700}
.email-input{left:23px;top:443px;width:178px;height:21px;background:#fff;border:2px solid #7a8a92;border-radius:11px;font-size:13px;line-height:17px;padding-left:8px;color:#888}
.email-input svg{position:absolute;right:8px;top:2px}
.subscribe-btn{left:210px;top:442px;width:83px;height:23px;background:linear-gradient(180deg,#1b8fbf,var(--brand-dark));border:2px solid var(--brand-deep);border-radius:8px;color:#062433;font-weight:700;font-size:14px;line-height:19px;text-align:center}

.promo-banner{left:24px;top:576px;width:296px;height:141px;border-radius:4px;background:linear-gradient(100deg,#3f6fa8 0%,#b34a3c 35%,#4f8aa0 65%,#cfd8dc 100%)}
.promo-banner .caption{position:absolute;left:118px;top:58px;width:176px;height:60px;background:rgba(20,20,20,.75);color:#fff;padding:6px 8px}
.caption b{display:block;font:400 15px "Open Sans",sans-serif;color:#3aa9e6}
.caption span{font:8px/10px "Open Sans",sans-serif}
.side-photo{left:34px;width:286px;height:103px;background:linear-gradient(180deg,#f0dfb5,#e3cc98);box-shadow:0 0 0 4px #7fa8b2}

.section-title{left:352px;top:124px;font-size:14px;font-weight:700}
.map{left:349px;top:145px;width:610px;height:281px;background:#e8e6df;border:1px solid #ccc}

.carousel{left:349px;top:437px;width:601px;height:182px;background:var(--carousel-bg);border:1px solid #5c8fa3}
.carousel-arrow{top:437px}
.thumb{top:453px;width:118px;height:87px;background:linear-gradient(180deg,#8cb6d6 0%,#d9c79a 40%,#c7b283 100%)}
.card-text{top:562px;width:130px;font:11px/13px "Open Sans",sans-serif;color:var(--muted)}
.card-text strong{display:block;font-weight:700;margin-bottom:14px;color:#222}
.card-text .row{display:flex;justify-content:space-between;width:98px}

.listing{left:337px;width:630px;height:97px}
.listing .photo{position:absolute;left:0;top:0;width:128px;height:97px;background:linear-gradient(180deg,#cfe2f0 0%,#2f78c4 25%,#1e60ad 100%)}
.listing h3{position:absolute;left:142px;top:7px;font-size:14px;font-weight:700}
.listing .meta{position:absolute;left:142px;top:35px;font-size:11px}
.listing .meta b{margin-left:42px}
.listing p{position:absolute;left:142px;font-size:11px;white-space:nowrap;width:488px;overflow:hidden}

.site-footer{left:0;top:1110px;width:995px;height:90px;background:var(--footer);color:#fff;font-family:"Open Sans",sans-serif}
.footer-col{top:11px;font-size:11px;line-height:13px}
.legal{left:20px;top:64px;font-size:8.5px;font-weight:700;line-height:11px}
</style>
</head>
<body>

<header class="site-header abs">
  <div class="brand-name abs">CrateHarbor</div>
  <nav class="top-links abs"><a>Create an Account</a><a>Login</a><a>AboutCrateHarbor.com</a><a>Contact Us&nbsp; (555) 014-2290</a></nav>
  <nav class="main-nav">
    <a style="left:34px;width:173px">20' Shipping Containers</a>
    <a style="left:222px;width:172px">40' Shipping Containers</a>
    <a style="left:410px;width:174px">40' High Cube Containers</a>
    <a style="left:600px;width:144px">Open Top Containers</a>
    <a style="left:761px;width:198px">How to Buy a Shipping Container</a>
  </nav>
  <div class="search-input abs">City, State or Country
    <svg class="abs" style="right:6px;top:2px" width="13" height="13" viewBox="0 0 13 13"><circle cx="5" cy="5" r="3.8" fill="none" stroke="#444" stroke-width="1.5"/><path d="M8 8l4 4" stroke="#444" stroke-width="2"/></svg>
  </div>
  <div class="select abs" style="left:640px;width:100px">Container Type<svg width="14" height="12" viewBox="0 0 14 12"><path d="M1 1h12L7 11z" fill="#444"/></svg></div>
  <div class="select abs" style="left:757px;width:57px">Untits<svg width="14" height="12" viewBox="0 0 14 12"><path d="M1 1h12L7 11z" fill="#444"/></svg></div>
  <div class="search-btn abs">Search</div>
</header>

<main class="content-panel abs"></main>

<nav class="side-nav">
  <a style="top:146px">How to Buy Shipping Containers</a>
  <a style="top:180px">New Listings</a>
  <a style="top:213px">News and Articles</a>
  <a style="top:248px">About CrateHarbor.com</a>
  <a style="top:282px">Container Weights and Dimensions</a>
  <a style="top:313px">CrateHarbor.com FAQs</a>
  <a style="top:346px">Shipping Container Terms</a>
  <a style="top:380px">How to Sell Your Containers</a>
</nav>

<div class="newsletter-label abs">Subscribe to Our Newsletter</div>
<div class="email-input abs">Enter Email
  <svg width="14" height="14" viewBox="0 0 13 13"><circle cx="5" cy="5" r="3.8" fill="none" stroke="#555" stroke-width="1.5"/><path d="M8 8l4 4" stroke="#555" stroke-width="2"/></svg>
</div>
<div class="subscribe-btn abs">Subscribe</div>

<div class="promo-banner abs" role="img" aria-label="Photo of stacked shipping containers in a port yard">
  <div class="caption"><b>containers for sale</b><span>Our storage containers are ideal for storing materials that need to stay dry and secure.</span></div>
</div>
<div class="side-photo abs" style="top:738px" role="img" aria-label="Side view of a beige branded shipping container"></div>
<div class="side-photo abs" style="top:864px" role="img" aria-label="Side view of a beige branded shipping container"></div>
<div class="side-photo abs" style="top:980px" role="img" aria-label="Side view of a beige branded shipping container"></div>

<h2 class="section-title abs">LOCATE US</h2>
<div class="map abs" role="img" aria-label="Street map of the shopping district showing the store location"></div>

<section class="carousel abs"></section>
<svg class="carousel-arrow abs" style="left:336px" width="24" height="120" viewBox="0 0 24 120"><path d="M24 0v120L0 50z" fill="var(--brand-dark)"/></svg>
<svg class="carousel-arrow abs" style="left:949px" width="24" height="120" viewBox="0 0 24 120"><path d="M0 0v120L24 50z" fill="var(--brand-dark)"/></svg>

<div class="thumb abs" style="left:376px" role="img" aria-label="Beige shipping container photo"></div>
<div class="thumb abs" style="left:516px" role="img" aria-label="Beige shipping container photo"></div>
<div class="thumb abs" style="left:666px" role="img" aria-label="Beige shipping container photo"></div>
<div class="thumb abs" style="left:815px" role="img" aria-label="Beige shipping container photo"></div>

<div class="card-text abs" style="left:378px"><strong>Listing Name</strong>Container Type<div class="row"><span>Location</span><span>Price $</span></div></div>
<div class="card-text abs" style="left:518px"><strong>Listing Name</strong>Container Type<div class="row"><span>Location</span><span>Price $</span></div></div>
<div class="card-text abs" style="left:668px"><strong>Listing Name</strong>Container Type<div class="row"><span>Location</span><span>Price $</span></div></div>
<div class="card-text abs" style="left:817px"><strong>Listing Name</strong>Container Type<div class="row"><span>Location</span><span>Price $</span></div></div>

<article class="listing abs" style="top:648px">
  <div class="photo" role="img" aria-label="Blue shipping container photo"></div>
  <h3>Listing Name</h3><div class="meta">Container Type<b>Price $</b></div>
  <p style="top:48px">Lorem ipsum dolor sit amet, consectetur adipiscing elit. Morbi semper, augue ut suscipit faucibus, od</p>
  <p style="top:72px">Lorem ipsum dolor sit amet, consectetur adipiscing elit. Morbi semper, augue ut suscipit faucibus, od</p>
</article>
<article class="listing abs" style="top:760px">
  <div class="photo" role="img" aria-label="Blue shipping container photo"></div>
  <h3>Listing Name</h3><div class="meta">Container Type<b>Price $</b></div>
  <p style="top:48px">Lorem ipsum dolor sit amet, consectetur adipiscing elit. Morbi semper, augue ut suscipit faucibus, od</p>
  <p style="top:72px">Lorem ipsum dolor sit amet, consectetur adipiscing elit. Morbi semper, augue ut suscipit faucibus, od</p>
</article>
<article class="listing abs" style="top:872px">
  <div class="photo" role="img" aria-label="Blue shipping container photo"></div>
  <h3>Listing Name</h3><div class="meta">Container Type<b>Price $</b></div>
  <p style="top:48px">Lorem ipsum dolor sit amet, consectetur adipiscing elit. Morbi semper, augue ut suscipit faucibus, od</p>
  <p style="top:72px">Lorem ipsum dolor sit amet, consectetur adipiscing elit. Morbi semper, augue ut suscipit faucibus, od</p>
</article>
<article class="listing abs" style="top:986px">
  <div class="photo" role="img" aria-label="Blue shipping container photo"></div>
  <h3>Listing Name</h3><div class="meta">Container Type<b>Price $</b></div>
  <p style="top:48px">Lorem ipsum dolor sit amet, consectetur adipiscing elit. Morbi semper, augue ut suscipit faucibus, od</p>
  <p style="top:72px">Lorem ipsum dolor sit amet, consectetur adipiscing elit. Morbi semper, augue ut suscipit faucibus, od</p>
</article>

<footer class="site-footer abs">
  <div class="footer-col abs" style="left:33px">Privacy Policy<br>User Agreement<br>Help</div>
  <div class="footer-col abs" style="left:159px">About CrateHarbor.com<br>News and Articles<br>Contact Information</div>
  <div class="footer-col abs" style="left:323px">Container Dimensions and Weights<br>Glossary</div>
  <div class="footer-col abs" style="left:518px">Browse Locations</div>
  <div class="legal abs">Copyright © 2011-2013 CrateHarbor, Inc. All Rights Reserved. CrateHarbor.com is a trademark of CrateHarbor Inc.<br>Designated trademarks and brands are the property of their respective owners. Use of this Web site constitutes acceptance of the CrateHarbor user agreement and privacy policy.</div>
</footer>

</body>
</html>
```